Iconset für Bestellablauf eines Fensterlieferanten/Produzenten
Zielgruppe
Guten Tag,
wir sind Fenster Hersteller und Produzent von edlen Aluminiumfenstern basierend auf Venrak Profilen. Unsere Qualität der Produkte, unser Service und Zuverlässigkeit stehen dabei an oberster Stelle.
Aufgabenstellung
Wir suchen ein Iconset für eine Auflistung aller Punkte unseres Bestellablaufes. Dieser Bestellablauf ist auf folgender Webseite zu sehen: http://www.rahmenwerk17.example/bestellablauf
Designlich sollte es auch zu folgender Webseite passen: http://www.glaspanel17.example/
Es sind neun Punkte, die jeweils ein schönes Icon benötigen, in dem oben angegebenem Link können Sie die Tätigkeiten der jeweiligen Punkte einsehen. Diesen Tätigkeiten sollte jedes Icon natürlich entsprechen.
Wir sind gespannt auf Ihre Vorschläge!

```html
<!DOCTYPE html>
<html lang="de">
<head>
<meta charset="utf-8">
<title>Rahmenwerk17 – Bestellablauf</title>
<link rel="stylesheet" href="https://fonts.googleapis.com/css2?family=Arimo:wght@400;700&display=swap">
<style>
  :root {
    --ink: #222;
    --text: #333;
    --heading: #4a4a4a;
    --brand-navy: #1d2a4a;
    --link-blue: #1f5fa6;
    --rule: #cfcfcf;
    --nav-bg: rgba(20, 24, 30, 0.72);
    --badge-grey: #4a4f55;
    --new-red: #d6342c;
    --icon-line: #2a3550;
    --icon-accent: #4f7fb5;
  }
  * { box-sizing: border-box; margin: 0; padding: 0; }
  html, body { width: 848px; height: 1200px; overflow: hidden; background: #fff; }
  body { position: relative; font-family: "Arimo", Arial, sans-serif; color: var(--text); }

  .site-logo {
    position: absolute; left: 64px; top: 72px;
    font-size: 31px; font-weight: 400; color: var(--brand-navy); letter-spacing: -0.5px;
  }
  .site-logo small { font-size: 13px; }

  .hero { position: absolute; left: 0; top: 134px; width: 848px; height: 231px; }
  .hero-photo { position: absolute; top: 0; height: 231px; }
  .hero-photo.house { left: 0; width: 325px; background: linear-gradient(160deg, #6f89a8 0%, #9fb0c4 40%, #3f4b58 100%); }
  .hero-photo.interior { left: 329px; width: 455px; background: linear-gradient(180deg, #d9dde2 0%, #b9bfc6 55%, #5b6470 100%); }
  .hero-photo.night { left: 788px; width: 60px; background: linear-gradient(180deg, #2b3d55 0%, #1a2533 100%); }

  .main-nav {
    position: absolute; left: 25px; top: 152px; width: 830px; height: 42px;
    border: 2px solid #fff; border-right: none; background: var(--nav-bg);
    display: flex; align-items: center; padding-left: 12px; gap: 22px;
  }
  .main-nav a, .nav-overflow {
    color: #fff; text-decoration: none; font-size: 13px; font-weight: 700; white-space: nowrap; letter-spacing: -0.2px;
  }
  .nav-overflow { position: absolute; left: 36px; top: 204px; }

  .sidebar { position: absolute; left: 0; top: 365px; width: 212px; height: 835px; border-right: 1px solid var(--rule); }
  .sidebar h2 { position: absolute; left: 11px; top: 32px; font-size: 18px; font-weight: 400; color: var(--link-blue); }
  .page-menu { position: absolute; left: 14px; top: 84px; list-style: none; }
  .page-menu li { height: 24px; font-size: 13.5px; color: var(--ink); line-height: 24px; }
  .page-menu li.current {
    background: var(--brand-navy); color: #fff; font-weight: 700;
    margin-left: -2px; padding-left: 2px; width: 95px; height: 22px; line-height: 22px; margin-bottom: 2px;
  }
  .partner-badge {
    position: absolute; left: 11px; top: 383px; width: 119px; height: 54px;
    background: var(--badge-grey); color: #fff; font-size: 17px; font-weight: 700;
    display: flex; align-items: center; justify-content: center; letter-spacing: 1px;
  }
  .partner-link { position: absolute; left: 11px; top: 452px; font-size: 13px; color: var(--ink); display: flex; align-items: center; gap: 5px; }
  .partner-link .new-tag { width: 17px; height: 9px; background: var(--new-red); border-radius: 2px; }

  .content { position: absolute; left: 237px; top: 365px; width: 611px; height: 835px; overflow: hidden; }
  .content h1 { position: absolute; left: 0; top: 32px; font-size: 22px; font-weight: 400; color: var(--heading); white-space: nowrap; }
  .content .lead { position: absolute; left: 0; top: 77px; font-size: 19px; font-weight: 700; color: var(--heading); white-space: nowrap; }
  .content .intro { position: absolute; left: 0; top: 111px; width: 780px; font-size: 13px; line-height: 22.5px; color: var(--ink); }

  .order-steps { list-style: none; }
  .order-step { position: absolute; left: 0; width: 780px; }
  .step-icon { position: absolute; left: 2px; top: -2px; width: 46px; height: 46px; }
  .step-icon * { fill: none; stroke: var(--icon-line); stroke-width: 1.6; stroke-linecap: round; stroke-linejoin: round; }
  .step-icon .accent { stroke: var(--icon-accent); }
  .step-icon .ground { stroke: var(--icon-accent); stroke-width: 2; }
  .step-icon .solid { fill: var(--icon-accent); stroke: none; }
  .order-step p { position: absolute; left: 56px; top: 0; width: 720px; font-size: 13px; line-height: 22px; color: var(--ink); }
  .order-step::after {
    content: ""; position: absolute; left: 20px; width: 760px; border-top: 1px solid var(--rule);
    top: var(--rule-offset, 50px);
  }
</style>
</head>
<body>

<div class="site-logo">Rahmenwerk17<small>.com</small></div>

<div class="hero">
  <div class="hero-photo house" role="img" aria-label="Modernes weißes Haus mit großen Aluminiumfenstern am Abend"></div>
  <div class="hero-photo interior" role="img" aria-label="Heller Wohnraum mit raumhoher Fensterfront und Vorhängen"></div>
  <div class="hero-photo night" role="img" aria-label="Fassade bei Nacht"></div>
  <nav class="main-nav">
    <a href="#">HOME</a>
    <a href="#">ALUMINIUMFENSTER</a>
    <a href="#">PREISLISTEN</a>
    <a href="#">REFERENZEN</a>
    <a href="#">MONTAGE</a>
    <a href="#">PARTNER</a>
    <a href="#">SERVICE</a>
    <a href="#">UNTERNEHMEN</a>
  </nav>
  <span class="nav-overflow">KONTAKT</span>
</div>

<aside class="sidebar">
  <h2>Seiten</h2>
  <ul class="page-menu">
    <li>Home</li>
    <li>Aluminiumfenster</li>
    <li>Preislisten</li>
    <li>Referenzen</li>
    <li>Montage</li>
    <li>Partner</li>
    <li>Service</li>
    <li>Unternehmen</li>
    <li>Standorte</li>
    <li class="current">Bestellablauf</li>
    <li>Kontakt</li>
  </ul>
  <div class="partner-badge">VENRAK</div>
  <div class="partner-link">Venrak Alu Fenster <span class="new-tag"></span></div>
</aside>

<main class="content">
  <h1>Bestellablauf eines Auftrages</h1>
  <p class="lead">Rahmenwerk 17 setzt in Sachen Preis/Leistung und Servicequalität neue Maßstäbe</p>
  <p class="intro">Das bedeutet für uns vor allem kompetente Beratung und Bearbeitung Ihrer Bestellung. Aus diesem Grund bieten wir<br>
  Serviceleistungen, damit wir Ihnen einen angenehmen und reibungslosen Bestellablauf anbieten können. Hier der<br>
  Bestellablaufprozess in einzelnen Punkten vor.</p>

  <ol class="order-steps">
    <li class="order-step" style="top:195px; --rule-offset:50px">
      <svg class="step-icon" viewBox="0 0 46 46" role="img" aria-label="Icon: Anfrage mit Zeichnung senden">
        <path d="M10 6 H26 L32 12 V34 H10 Z"/><path d="M26 6 V12 H32"/>
        <path class="accent" d="M14 17 H27 M14 22 H27 M14 27 H22"/>
        <path class="accent" d="M28 26 L40 18 M40 18 L34 18 M40 18 L38 24"/>
        <path class="ground" d="M2 41 Q23 35 44 41"/>
      </svg>
      <p>Stellen Sie uns einfach eine Anfrage zu Ihrem Anliegen an Rahmenwerk17 mit den dazugehörigen Maßen oder<br>senden uns einfach die CAD oder Architektur-Zeichnung zu.</p>
    </li>
    <li class="order-step" style="top:259px; --rule-offset:75px">
      <svg class="step-icon" viewBox="0 0 46 46" role="img" aria-label="Icon: Angebot wird erarbeitet und geprüft">
        <path d="M8 5 H28 V34 H8 Z"/>
        <path class="accent" d="M12 12 H24 M12 17 H24 M12 22 H19"/>
        <circle cx="29" cy="26" r="7"/><path d="M34 31 L40 37"/>
        <path class="ground" d="M2 41 Q23 35 44 41"/>
      </svg>
      <p>Wir erarbeiten Ihr Angebot zu Aluminium Elementen in möglichst kurzer Zeit und prüfen es. Sollte<br>spezieller Absprachebedarf existieren, so kontaktieren wir Sie und bieten Ihnen Vorschläge an. Nach<br>ausgiebiger Prüfung Ihrer Anfrage lassen wir Ihnen ein Angebot zukommen.</p>
    </li>
    <li class="order-step" style="top:351px; --rule-offset:47px">
      <svg class="step-icon" viewBox="0 0 46 46" role="img" aria-label="Icon: Zusammenarbeit wird vereinbart">
        <path d="M3 18 L10 15 L18 21 L14 26"/>
        <path d="M43 18 L36 15 L26 16 L19 21 Q21 24 25 21 L29 20 L37 27"/>
        <path class="accent" d="M14 26 L19 30 M18 24 L23 28 M22 23 L27 27 M19 30 L23 32 L37 27"/>
        <path class="ground" d="M2 41 Q23 35 44 41"/>
      </svg>
      <p>Wenn Ihnen die Konditionen und die Zusammenarbeit von Rahmenwerk17 zusagt, setzen wir gemeinsam mit<br>dem Bestellablauf fortfahren können.</p>
    </li>
    <li class="order-step" style="top:413px; --rule-offset:50px">
      <svg class="step-icon" viewBox="0 0 46 46" role="img" aria-label="Icon: Außendienst berät vor Ort">
        <path d="M23 36 C15 26 12 21 12 16 A11 11 0 0 1 34 16 C34 21 31 26 23 36 Z"/>
        <circle class="accent" cx="23" cy="16" r="4.5"/>
        <path class="ground" d="M2 41 Q23 35 44 41"/>
      </svg>
      <p>Ein Außendienstmitarbeiter kommt auf Wunsch bei Ihnen vorbei um technische Details zu klären und<br>um Sie bestmöglich über unsere Aluminiumprofile und Materialien zu unterstützen und zu beraten.</p>
    </li>
    <li class="order-step" style="top:477px; --rule-offset:49px">
      <svg class="step-icon" viewBox="0 0 46 46" role="img" aria-label="Icon: Feinaufmaß am Bauvorhaben">
        <path d="M9 5 H29 V27 H9 Z M19 5 V27 M9 16 H29"/>
        <path class="accent" d="M5 33 H41 V38 H5 Z M11 33 V35.5 M17 33 V36.5 M23 33 V35.5 M29 33 V36.5 M35 33 V35.5"/>
        <path d="M34 8 V24 M32 10 L34 8 L36 10 M32 22 L34 24 L36 22"/>
      </svg>
      <p>Nachdem Sie uns einen Auftrag zur Aluminiumfenster Produktion erteilt haben, wird ein<br>Feinaufmaß an Ihrem Bauvorhaben durchgeführt.</p>
    </li>
    <li class="order-step" style="top:543px; --rule-offset:50px">
      <svg class="step-icon" viewBox="0 0 46 46" role="img" aria-label="Icon: Fertigung in der Produktion">
        <path d="M7 35 V20 L15 25 V20 L23 25 V20 L31 25 V8 H36 V35 Z"/>
        <path class="accent" d="M11 30 H14 M18 30 H21 M25 30 H28"/>
        <path class="accent" d="M33 5 Q36 2 39 4"/>
        <path class="ground" d="M2 41 Q23 35 44 41"/>
      </svg>
      <p>Nach Festlegung aller technischen Details und Konditionen beginnt die Fertigung der Fenster. Die Dauer<br>der Fertigung beträgt je nach Umfang 6 bis 8 Wochen.</p>
    </li>
    <li class="order-step" style="top:608px; --rule-offset:50px">
      <svg class="step-icon" viewBox="0 0 46 46" role="img" aria-label="Icon: Lieferung per LKW">
        <path d="M4 12 H28 V31 H4 Z"/>
        <path d="M28 18 H36 L42 25 V31 H28"/>
        <path class="accent" d="M31 20 H35 L39 25 H31 Z"/>
        <circle cx="12" cy="32" r="3.5"/><circle cx="35" cy="32" r="3.5"/>
        <path class="ground" d="M2 41 Q23 35 44 41"/>
      </svg>
      <p>Ihre Ware verlässt mit dem diensteigenen LKW unsere Rahmenwerk17 Produktionsstätte und wird an die<br>vorgegebenen Lieferadresse angeliefert. Den Lieferort für die Fenster bestimmen natürlich Sie.</p>
    </li>
    <li class="order-step" style="top:673px; --rule-offset:50px">
      <svg class="step-icon" viewBox="0 0 46 46" role="img" aria-label="Icon: Montage der Fenster">
        <path d="M12 36 V6 M16 36 V6 M12 12 L16 16 M16 12 L12 16 M12 22 L16 26 M16 22 L12 26"/>
        <path d="M6 6 H40 M16 6 L10 11 M14 6 L6 9"/>
        <path class="accent" d="M34 6 V16"/>
        <path class="accent" d="M29 16 H39 V26 H29 Z M34 16 V26"/>
        <path class="ground" d="M2 41 Q23 35 44 41"/>
      </svg>
      <p>Bei hinzugebuchter Montageleistung erfolgt im Anschluss der Lieferung die Montage. Wir<br>übernehmen gerne diese Arbeit für Sie. Der Termin wird mit Ihnen telefonisch festgelegt.</p>
    </li>
    <li class="order-step" style="top:738px; --rule-offset:90px">
      <svg class="step-icon" viewBox="0 0 46 46" role="img" aria-label="Icon: Abschluss und Übergabe">
        <circle cx="23" cy="19" r="14"/>
        <path class="accent" d="M16 19 L21 24 L31 13"/>
        <path class="ground" d="M2 41 Q23 35 44 41"/>
      </svg>
      <p>Nach Abschluss aller ausgeführten Aufgaben, der Fensterproduktion, Lieferung und ggf. Montage ist alles<br>fertiggestellt. Nach der Fertigstellung erhalten Sie einen umfassenden Zugang zu unserem Service, der<br>Rahmenwerk17 beratend zur Seite steht.</p>
    </li>
  </ol>
</main>

</body>
</html>
```